Design website home page for pathology consulting company

Starting a new consulting company with anatomic pathologists focused on expert diagnosis and second opinions on difficult pathology cases. In the near future we will be incorporating next generation diagnostics for rare diseases of childhood into the business. These include discovery and testing of DNA for mutations.

The company is formed around one of the best known pathologists in the world named Marcus "Buddy" Halvorsen. The name of the company is "BuddyScope"

We had a logo design by Sketchfold - it is great. I will attach file as soon as I have it (contest ending today). Our company is medical, uses microscopes, DNA, probably will focus on childhood diseases but not solely on childhood diseases. we're not particularly conservative, but the customers we want to appeal to include older practicing pathologists as well as patients (sometimes parents) looking for second opinions.

Think a group of expert doctors diagnosing disease through the microscope and through DNA technology, ages ranging from 35-75 all trained by the best pathologist in the world - "Buddy"

We receive glass slides from diseases from patients all over the world from docs who need an expert to tell them what is the diagnosis. So "path to the diagnosis" is also part of the company marketing message.

We want the website design to describe our company but be very simple to find what one is looking for as we will use it as the launch page to:
1) order services
2) check results/reports
3) set up new account
4) speak with one of the pathologists
5) see our test menu
6) access our educational material/webinars

Update - looking for home page design and then finalists will ask for second page design to keep with theme - ok?

Reason: realized this project isn't web design but web home page design - thanks

Reason: Holidays for some in next two weeks

Reason: Hot discussion among collaborators for a few of the submissions. Will provide detail individually this weekend. Thanks so much for all the submissions!

Target Market(s)

Referring pathologists, physicians who want second opinions on pathology disease diagnosis, patients who have had biopsies (either patients themselves or parents of patients), generally high education level

Industry/Entity Type

Marketing

Requirements
Must have
• BuddyScope
Next Generation Pathology Consultants

```html
<!DOCTYPE html>
<html lang="en">
<head>
<meta charset="utf-8">
<title>BuddyScope — Next Generation Pathology Consultants</title>
<link href="https://fonts.googleapis.com/css2?family=PT+Sans:wght@400;700&family=Noto+Sans:wght@400&display=swap" rel="stylesheet">
<style>
:root{
  --brand:#0375b9;
  --brand-dark:#045a8e;
  --heading-blue:#0b5e8e;
  --heading-grey:#3c3c3c;
  --text:#3e3e3e;
  --link:#1a8ad6;
  --rule:#d4d4d4;
  --footer:#ebebeb;
  --news:#1b8fe0;
  --services:#2fd8b6;
  --careers:#2fe067;
  --photo-a:#c9b9a8;
}
*{margin:0;padding:0;box-sizing:border-box}
html,body{width:1200px;height:1035px;overflow:hidden;background:#fff}
body{position:relative;font-family:"Noto Sans",Verdana,sans-serif;color:var(--text);font-size:12.5px;line-height:18px}
a{color:var(--link)}
.abs{position:absolute}
.topbar{left:0;top:0;width:1200px;height:50px;background:var(--brand)}
.home-tab{left:151px;top:0;width:58px;height:54px;background:var(--brand-dark)}
.main-nav{right:108px;top:16px;display:flex;gap:20px;font-family:"PT Sans",sans-serif;font-size:14px;color:#fff}
.main-nav span:last-child{margin-left:4px}
.header-band{left:0;top:50px;width:1200px;height:285px;background:linear-gradient(#eef2f4,#fff 30px);border-bottom:1px solid var(--rule)}
.brand-mark{left:216px;top:106px;width:96px;height:96px;border-radius:50%;background:#a4a7ab}
.brand-name{left:148px;top:210px;font-family:"PT Sans",sans-serif;font-size:37px;line-height:40px;color:var(--brand-dark);letter-spacing:2.2px}
.brand-tag{left:150px;top:252px;font-family:"PT Sans",sans-serif;font-size:14px;line-height:18px;color:#6b6b6b}
.slider{left:414px;top:70px;width:678px;height:282px;background:#fff;border:1px solid #ddd}
.slider-photo{left:4px;top:5px;width:668px;height:234px;background:linear-gradient(100deg,#8a6a4a,#c9a785 35%,#e7d7c4 60%,#3d6ea8)}
.slider-caption{right:97px;top:250px;font-family:"PT Sans",sans-serif;font-size:14px;color:#333}
.slider-arrow{top:246px}
.slider-shadow{left:440px;top:352px;width:640px;height:20px;background:radial-gradient(ellipse at top,rgba(0,0,0,.25),transparent 70%)}
h2{font-family:"PT Sans",sans-serif;font-weight:700;font-size:25px;line-height:28px}
.links-title{left:150px;top:380px;color:var(--heading-grey)}
.quick-links{left:150px;top:418px;list-style:none;width:240px}
.quick-links li{position:relative;padding-left:20px;height:31px;font-size:12.5px;line-height:17px;letter-spacing:.2px}
.quick-links li.two{height:40px}
.quick-links svg{position:absolute;left:0;top:3px}
.dots{left:264px;top:440px;width:150px;border-top:1px dotted #bbb}
.welcome-title{left:416px;top:380px;color:var(--heading-blue)}
.like-btn{left:752px;top:384px;height:19px;padding:0 6px;border:1px solid #c5c9d4;border-radius:2px;font-size:11px;line-height:17px;color:#3b5998;background:#eef0f6}
.like-count{left:802px;top:385px;width:21px;height:18px;border:1px solid #ccc;font-size:10px;text-align:center;line-height:16px}
.fav-btn{left:830px;top:383px;height:20px;padding:0 6px 0 22px;border:1px solid #ccc;border-radius:3px;background:linear-gradient(#fff,#e6e6e6);font-size:11px;font-weight:700;line-height:18px;color:#444}
.fav-btn svg{position:absolute;left:6px;top:4px}
.welcome-photo{left:415px;top:425px;width:155px;height:156px;background:linear-gradient(160deg,var(--photo-a),#efe4d9 55%,#6b5a50);box-shadow:0 5px 6px -3px rgba(0,0,0,.4)}
.dots2{left:570px;top:440px;width:20px;border-top:1px dotted #bbb}
.welcome-text{left:592px;top:429px;width:492px;font-size:12.5px;line-height:18px;letter-spacing:.4px}
.welcome-text p+p{margin-top:14px}
.col-title{color:var(--heading-blue);padding-bottom:7px}
.col{top:643px;font-size:12.5px;line-height:18px;letter-spacing:.4px}
.col p{margin-bottom:18px}
.col-body{margin-top:12px}
.news{left:414px;width:210px}
.news h2{border-bottom:5px solid var(--news)}
.services{left:638px;width:210px}
.services h2{border-bottom:5px solid var(--services)}
.careers{left:860px;width:231px}
.careers h2{border-bottom:5px solid var(--careers)}
.careers-photo{width:226px;height:82px;margin:10px 0 15px;background:linear-gradient(90deg,#5d6670,#a89486 45%,#e8e8e8)}
.downloads-title{left:148px;top:689px;color:var(--heading-grey)}
.downloads{left:150px;top:727px;list-style:none}
.downloads li{position:relative;padding-left:28px;height:30px;font-size:12.5px;line-height:20px;letter-spacing:.3px}
.downloads svg{position:absolute;left:0;top:1px}
.footer{left:0;top:923px;width:1200px;height:112px;background:var(--footer);border-top:1px solid #fff;box-shadow:0 -1px 0 #d8d8d8}
.copyright{left:150px;top:963px;font-size:10px;color:#555}
.footer-nav{left:150px;top:981px;font-size:10px;color:#555;word-spacing:2px}
.footer-nav a{text-decoration:none}
.social{right:110px;top:965px;display:flex;gap:14px}
.social span{width:26px;height:26px;border-radius:4px;background:var(--c)}
</style>
</head>
<body>
<div class="abs topbar"></div>
<div class="abs home-tab">
  <svg width="58" height="54" viewBox="0 0 58 54"><path d="M29 12 L16 24 h4 v12 h7 v-7 h4 v7 h7 V24 h4 Z" fill="#fff"/></svg>
</div>
<nav class="abs main-nav"><span>About Us</span><span>Services</span><span>Gallery</span><span>Careers</span><span>Trainings</span><span>FAQ</span><span>Contacts</span></nav>

<header class="abs header-band"></header>
<div class="abs brand-mark"></div>
<div class="abs brand-name">BuddyScope</div>
<div class="abs brand-tag">Next Generation Pathology Consultants</div>

<div class="abs slider-shadow"></div>
<section class="abs slider">
  <div class="abs slider-photo" role="img" aria-label="Consultant with headset working at an office desk"></div>
  <div class="abs slider-caption">100% Service Guarantee</div>
  <svg class="abs slider-arrow" style="left:596px" width="28" height="28" viewBox="0 0 28 28"><circle cx="14" cy="14" r="12.5" fill="#fff" stroke="var(--brand)" stroke-width="2"/><path d="M18 8 L9 14 L18 20 Z" fill="var(--brand)"/></svg>
  <svg class="abs slider-arrow" style="left:636px" width="28" height="28" viewBox="0 0 28 28"><circle cx="14" cy="14" r="12.5" fill="#fff" stroke="var(--brand)" stroke-width="2"/><path d="M10 8 L19 14 L10 20 Z" fill="var(--brand)"/></svg>
</section>

<h2 class="abs links-title">LINKS</h2>
<div class="abs dots"></div>
<ul class="abs quick-links">
  <li><svg width="12" height="12"><circle cx="6" cy="6" r="5" fill="none" stroke="var(--link)"/><path d="M3.5 6h5M6 3.5v5" stroke="var(--link)"/></svg>order services</li>
  <li><svg width="12" height="12"><circle cx="6" cy="6" r="5" fill="none" stroke="var(--link)"/><path d="M3.5 6h5M6 3.5v5" stroke="var(--link)"/></svg>check results/reports</li>
  <li><svg width="12" height="12"><circle cx="6" cy="6" r="5" fill="none" stroke="var(--link)"/><path d="M3.5 6h5M6 3.5v5" stroke="var(--link)"/></svg>set up new account</li>
  <li><svg width="12" height="12"><circle cx="6" cy="6" r="5" fill="none" stroke="var(--link)"/><path d="M3.5 6h5M6 3.5v5" stroke="var(--link)"/></svg>speak with one of the pathologists</li>
  <li><svg width="12" height="12"><circle cx="6" cy="6" r="5" fill="none" stroke="var(--link)"/><path d="M3.5 6h5M6 3.5v5" stroke="var(--link)"/></svg>see our test menu</li>
  <li class="two"><svg width="12" height="12"><circle cx="6" cy="6" r="5" fill="none" stroke="var(--link)"/><path d="M3.5 6h5M6 3.5v5" stroke="var(--link)"/></svg>access our educational<br>material/webinars</li>
</ul>

<h2 class="abs welcome-title">WELCOME TO BUDDYSCOPE</h2>
<div class="abs like-btn">Like</div>
<div class="abs like-count">0</div>
<div class="abs fav-btn"><svg width="12" height="11" viewBox="0 0 12 11"><path d="M6 10 L1.2 5.2 A2.7 2.7 0 0 1 6 2 A2.7 2.7 0 0 1 10.8 5.2 Z" fill="#999"/></svg>Favorite</div>
<div class="abs welcome-photo" role="img" aria-label="Smiling staff member wearing a headset"></div>
<div class="abs dots2"></div>
<div class="abs welcome-text">
  <p>Lorem ipsum dolor sit amet, consec tetuer adipiscing elit. Praesent<br>vesti bulummoles tie lacus. Aenean nonummy hendrerit mauris.</p>
  <p><a href="#">Fusce suscipit varius mi.</a> Cum sociis natoque penatibus et magnis dis parturient montes, nascetur ridiculus mus. Nulla dui. Fusce feugia malesuada odio. Morbi nunc odio, gravida at, cursus nec, luctus a, lorem. Maecenas tristique orci ac sem. Duis ultricies pharetra magna. Donec accumsan malesuada orci. Donec sit amet</p>
</div>

<section class="abs col news">
  <h2 class="col-title">NEWS</h2>
  <div class="col-body">
  <p>US pathology consulting firm to open office in RP.<br><a href="#">Read more</a></p>
  <p>RP plays host to world pathology conference.<br><a href="#">Read more</a></p>
  <p>Second opinions expect 25% growth.<br><a href="#">Read more</a></p>
  </div>
</section>
<section class="abs col services">
  <h2 class="col-title">SERVICES</h2>
  <div class="col-body">
  <p>BUDDYSCOPE is an expert pathology consulting company that relies on well trained expert pathologists.</p>
  <p>We tailor diagnostic services for each client individually.</p>
  <p><a href="#">Read more</a></p>
  </div>
</section>
<section class="abs col careers">
  <h2 class="col-title">CAREERS</h2>
  <div class="careers-photo" role="img" aria-label="Collage of staff at work in meetings and at desks"></div>
  <p>Morbi nunc odio, gravida at, cursus nec, luctus a, lorem. gravida at, cursus nec, luctus a, lorem</p>
  <p><a href="#">Read More</a></p>
</section>

<h2 class="abs downloads-title">DOWNLOADS</h2>
<ul class="abs downloads">
  <li><svg width="18" height="18"><rect width="18" height="18" rx="2" fill="#8a8a8a"/><path d="M9 3v7M5.5 7 9 10.5 12.5 7M4 13h10" stroke="#fff" stroke-width="1.8" fill="none"/></svg>Swift FTP Client Software</li>
  <li><svg width="18" height="18"><rect width="18" height="18" rx="2" fill="#8a8a8a"/><path d="M9 3v7M5.5 7 9 10.5 12.5 7M4 13h10" stroke="#fff" stroke-width="1.8" fill="none"/></svg>Secure FTP Server</li>
  <li><svg width="18" height="18"><rect width="18" height="18" rx="2" fill="#8a8a8a"/><path d="M9 3v7M5.5 7 9 10.5 12.5 7M4 13h10" stroke="#fff" stroke-width="1.8" fill="none"/></svg>Quick Scribe</li>
</ul>

<footer class="abs footer"></footer>
<div class="abs copyright">Copyright © 2006. BUDDYSCOPE ® All Rights Reserved.</div>
<nav class="abs footer-nav"><a href="#">Home</a> | <a href="#">About Us</a> | <a href="#">Services</a> | <a href="#">Gallery</a> | <a href="#">Careers</a> | <a href="#">Trainings</a> | <a href="#">FAQ</a> | <a href="#">Contacts</a></nav>
<div class="abs social">
  <span style="--c:#6cc4e8"></span><span style="--c:#3e5f78"></span><span style="--c:#3b5b9c"></span><span style="--c:#4b9ccf"></span><span style="--c:#1f5f9e"></span>
</div>
</body>
</html>
```